Brivomark Business Card

Brivomark is a young and energetic software development consultancy. We spend our time on the road working with clients on their sites an meeting new potential customers and employees!

We need a sharp, vibrant and memorable business card that will inspires those that receive it to look after it as it oozes quality and is a nice thing in its own right.

We like bold colours and distinctive design. So show us what you can do.

In terms of information on the card, it would be good to see:

* Our logo (Obviously :) )
* Employee name
* Email
* Website address
* Mobile number
* Full company name (Brivomark ltd)
* Registered company number
* Registered company address

Industry/Entity Type

Software

Requirements
Nice to have
• We are thinking that having a QR Code on the business card could be a good way of adding active marketing. It would be good to see if you are able to merge the kind of element in to your designs!

Maybe something special could be achieved using a visual QR Code like those produced at http://www.quenprint-example.com/ ? You have our media so feel free to have a play.

```html
<!DOCTYPE html>
<html lang="en">
<head>
<meta charset="utf-8">
<title>Brivomark Business Card</title>
<link href="https://fonts.googleapis.com/css2?family=Ubuntu:wght@300;400&display=swap" rel="stylesheet">
<style>
  :root {
    --brand-red: #c11f32;
    --brand-red-deep: #b5122a;
    --brand-pink: #f4c6cc;
    --tech-grey: #8e8e93;
    --text-grey: #8a8a8a;
    --icon-grey: #9a9a9a;
    --grid-grey: #a9a9a9;
    --grid-grey-light: #e6e6e6;
    --card-white: #ffffff;
    --stage-light: #ffffff;
    --stage-edge: #e9e9e9;
  }
  * { margin: 0; padding: 0; box-sizing: border-box; }
  html, body { width: 1200px; height: 900px; overflow: hidden; background: var(--stage-light); }
  body { font-family: "Ubuntu", sans-serif; position: relative; }

  .stage {
    position: absolute; left: 0; top: 0; width: 1200px; height: 695px;
    background: radial-gradient(ellipse 620px 420px at 600px 340px, var(--stage-light) 40%, var(--stage-edge) 100%);
  }

  .card {
    position: absolute; left: 402px; width: 400px; height: 230px;
    background: var(--card-white); border-radius: 28px; overflow: hidden;
    box-shadow: 0 2px 6px rgba(0,0,0,0.22);
  }
  .card--front { top: 100px; }
  .card--back { top: 368px; }

  .pixel-field--red {
    position: absolute; left: 0; top: 0; width: 200px; height: 230px;
    background: linear-gradient(90deg, var(--brand-red-deep) 0%, #d9616f 35%, #eea5ae 62%, var(--brand-pink) 80%, rgba(255,255,255,0) 100%);
  }
  .pixel-field--grey {
    position: absolute; right: 0; top: 0; width: 174px; height: 230px;
    background: linear-gradient(90deg, rgba(255,255,255,0) 0%, var(--grid-grey-light) 18%, #cfcfcf 55%, var(--grid-grey) 100%);
  }

  .wordmark {
    position: absolute; font-weight: 400; color: var(--brand-red);
    letter-spacing: 0.5px; line-height: 1; white-space: nowrap;
  }
  .card--front .wordmark { left: 212px; top: 102px; font-size: 26px; }
  .wordmark--footer { left: 826px; top: 775px; font-size: 43px; }

  .person-name {
    position: absolute; left: 77px; top: 27px; font-size: 19px;
    color: var(--brand-red); letter-spacing: 0.3px;
  }
  .person-role {
    position: absolute; left: 77px; top: 48px; font-size: 12px;
    color: var(--brand-red); letter-spacing: 0.3px;
  }
  .contact-list { position: absolute; left: 55px; top: 72px; list-style: none; }
  .contact-item {
    display: flex; align-items: center; height: 17.5px;
    font-size: 11.5px; font-weight: 300; color: var(--text-grey);
  }
  .contact-item svg { width: 12px; height: 12px; margin-right: 10px; fill: var(--icon-grey); }
  .company-address {
    position: absolute; left: 77px; top: 141px; font-size: 9.5px; font-weight: 300;
    line-height: 11.4px; color: var(--text-grey);
  }
</style>
</head>
<body>
  <div class="stage">
    <section class="card card--front">
      <div class="pixel-field--red" role="img" aria-label="Red mosaic of small squares fading from deep red to pale pink"></div>
      <div class="wordmark">BRIVOMARK</div>
    </section>

    <section class="card card--back">
      <div class="person-name">JOHN DOE</div>
      <div class="person-role">PRESIDENT</div>
      <ul class="contact-list">
        <li class="contact-item">
          <svg viewBox="0 0 12 12"><path d="M1 3h10v6.5H1z M1 3l5 3.6L11 3" fill="none" stroke="#9a9a9a" stroke-width="1.1"/><path d="M1 3h10L6 6.3z"/></svg>
          johndoe@brivomark-mail.com
        </li>
        <li class="contact-item">
          <svg viewBox="0 0 12 12"><circle cx="6" cy="6" r="4.8" fill="none" stroke="#9a9a9a" stroke-width="1.1"/><ellipse cx="6" cy="6" rx="2" ry="4.8" fill="none" stroke="#9a9a9a" stroke-width="1"/><path d="M1.2 6h9.6" stroke="#9a9a9a" stroke-width="1"/></svg>
          www.brivomark.com
        </li>
        <li class="contact-item">
          <svg viewBox="0 0 12 12"><rect x="3" y="1" width="6" height="10" rx="1.2"/><rect x="4" y="2.4" width="4" height="3.4" fill="#fff"/></svg>
          (000) 000-0000
        </li>
      </ul>
      <p class="company-address">Brivomark ltd<br>Lorem ipsum dolor<br>sit amet,<br>consectetuer a<br>dipiscing elit,<br>sed diam</p>
      <div class="pixel-field--grey" role="img" aria-label="Grey mosaic of small squares fading from light to mid grey"></div>
    </section>
  </div>

  <div class="wordmark wordmark--footer">BRIVOMARK</div>
</body>
</html>
```